Criação de Layout de Rótulo para Limpeza & Serviço para o lar
A empresa queria:
" ESTAMOS HÁ 42 ANOS FABRICANDO E VENDENDO OS MELHORES PRODUTOS DE LIMPEZA "

```html
<!DOCTYPE html>
<html lang="pt-BR">
<head>
<meta charset="UTF-8">
<title>Rótulo Aromatizante Lavanda</title>
<link rel="stylesheet" href="https://fonts.googleapis.com/css2?family=Montserrat:wght@400;500;600&family=Playfair+Display:wght@500&display=swap">
<style>
  :root {
    --page-bg: #eeeeee;
    --label-cream: #f6f3e6;
    --label-white: #fdfcf7;
    --band-lavender: #a58ec8;
    --band-text: #ffffff;
    --ink-dark: #2a2a2a;
    --sprig-tone-a: #e9e3d3;
    --sprig-tone-b: #ddd6ea;
    --rule-dark: #1c1c1c;
  }
  * { margin: 0; padding: 0; box-sizing: border-box; }
  html, body {
    width: 1200px;
    height: 1200px;
    overflow: hidden;
    background: var(--page-bg);
  }
  .label {
    position: absolute;
    left: 235px;
    top: 62px;
    width: 730px;
    height: 1076px;
    background: linear-gradient(180deg, var(--label-white) 0%, var(--label-cream) 100%);
    overflow: hidden;
  }
  .sprigs {
    position: absolute;
    top: 0;
    bottom: 60px;
    width: 110px;
    background: linear-gradient(180deg, var(--sprig-tone-b) 0%, var(--sprig-tone-a) 60%, transparent 100%);
    opacity: 0.7;
  }
  .sprigs--left { left: 0; }
  .sprigs--right { right: 0; }
  .band {
    position: absolute;
    left: 108px;
    top: 12px;
    width: 356px;
    height: 424px;
    background: var(--band-lavender);
    color: var(--band-text);
    font-family: "Montserrat", sans-serif;
  }
  .brand {
    position: absolute;
    left: 0;
    right: 0;
    top: 74px;
    text-align: center;
  }
  .brand__name {
    font-size: 48px;
    font-weight: 500;
    letter-spacing: 0.5px;
    display: inline-flex;
    align-items: center;
    gap: 10px;
  }
  .brand__dot {
    width: 10px;
    height: 10px;
    border-radius: 50%;
    background: var(--band-text);
  }
  .brand__tagline {
    margin-top: 6px;
    font-size: 11px;
    font-weight: 500;
    letter-spacing: 3px;
  }
  .product-type {
    position: absolute;
    left: 20px;
    top: 260px;
    width: 250px;
    font-size: 17px;
    font-weight: 500;
    letter-spacing: 1.5px;
  }
  .product-type__rule {
    height: 2px;
    background: var(--band-text);
    margin: 10px 0 20px;
    opacity: 0.85;
  }
  .scent {
    position: absolute;
    left: 0;
    right: 0;
    top: 850px;
    text-align: center;
    font-family: "Playfair Display", serif;
    font-weight: 500;
    font-size: 78px;
    color: var(--ink-dark);
  }
  .volume {
    position: absolute;
    left: 0;
    right: 0;
    top: 990px;
    text-align: center;
    font-family: "Montserrat", sans-serif;
    font-size: 26px;
    font-weight: 500;
    color: var(--ink-dark);
  }
  .bottom-rule {
    position: absolute;
    left: 0;
    right: 0;
    bottom: 14px;
    height: 4px;
    background: var(--rule-dark);
  }
</style>
</head>
<body>
  <div class="label">
    <div class="sprigs sprigs--left" role="img" aria-label="Ramos de lavanda desenhados em traço suave"></div>
    <div class="sprigs sprigs--right" role="img" aria-label="Ramos de lavanda desenhados em traço suave"></div>

    <div class="band">
      <div class="brand">
        <div class="brand__name"><span class="brand__dot"></span>Brisa Clara</div>
        <div class="brand__tagline">PRODUTOS DE LIMPEZA</div>
      </div>
      <div class="product-type">
        <div>AROMATIZANTE</div>
        <div class="product-type__rule"></div>
        <div>HOME SPRAY</div>
      </div>
    </div>

    <div class="scent">Lavanda</div>
    <div class="volume">260 ml</div>
    <div class="bottom-rule"></div>
  </div>
</body>
</html>
```